Bookkeeping business needs a digital and print flyer

We need a flyer to promote our virtual bookkeeping services to small and mid-sized businesses in the United States. We want the content and design of the flyer to be consistent with our website: www.brightledgerbookkeeping.example. We would like both a print version and a digital version of the flyer.

```html
<!DOCTYPE html>
<html lang="en">
<head>
<meta charset="utf-8">
<title>Bright Ledger Bookkeeping – Flyer</title>
<link href="https://fonts.googleapis.com/css2?family=Montserrat:wght@300;700;800&family=Roboto:wght@400;500;700&display=swap" rel="stylesheet">
<style>
:root{
  --yellow:#f9d423;
  --ink:#111111;
  --text:#222222;
  --paper:#ffffff;
  --backdrop:#ececec;
  --rule:#bdbdbd;
}
*{box-sizing:border-box;margin:0;padding:0}
html,body{width:960px;height:1200px;overflow:hidden}
body{background:var(--backdrop);font-family:"Roboto",Arial,sans-serif;color:var(--text);position:relative}
.page{position:absolute;top:302px;width:460px;height:596px;background:var(--paper);box-shadow:0 4px 14px rgba(0,0,0,.18);overflow:hidden;font-size:6.6px;line-height:1.3}
.page--front{left:14px}
.page--back{left:486px}
.abs{position:absolute}

/* front header */
.hero-photo{right:0;top:0;width:250px;height:155px;background:linear-gradient(120deg,#f3efea 0%,#d9d4cd 45%,#b9b2aa 70%,#d8cfc4 100%)}
.hero-fade{right:150px;top:0;width:110px;height:155px;background:linear-gradient(90deg,#fff,rgba(255,255,255,0))}
.brand{left:24px;top:38px;display:flex;align-items:center;gap:6px}
.brand__name{font-family:"Montserrat",Arial,sans-serif;font-weight:300;font-size:19px;letter-spacing:.5px;color:var(--ink);line-height:1}
.title{left:24px;top:80px;font-family:"Montserrat",Arial,sans-serif;font-weight:700;font-size:16px;line-height:1.3;color:var(--ink)}
.title span{color:var(--yellow);display:block}
.tagline{left:24px;top:130px;font-size:7px;width:140px}
.intro-band{left:0;top:155px;width:460px;height:49px;background:var(--ink);color:#fff;padding:9px 24px;font-size:6.8px;line-height:1.45}

.section-icon{flex:none;width:26px;height:26px;border:1.2px solid var(--ink);border-radius:50%}
.heading-y{font-family:"Montserrat",Arial,sans-serif;font-weight:700;color:var(--yellow);font-size:10px;line-height:1.3}
.lead{font-weight:700;font-size:6.8px;color:var(--ink)}
.checks{list-style:none}
.checks li{position:relative;padding-left:13px;margin-bottom:6px}
.checks li::before{content:"";position:absolute;left:0;top:.5px;width:6px;height:6px;border:.8px solid #444;border-radius:50%}
.checks li::after{content:"";position:absolute;left:2.2px;top:1.7px;width:1.6px;height:2.8px;border:solid #444;border-width:0 .8px .8px 0;transform:rotate(45deg)}

.col-left{left:24px;top:214px;width:190px}
.col-left .head{display:flex;align-items:center;gap:8px;margin-bottom:10px}
.col-left .lead{margin-bottom:8px}
.divider{left:222px;top:242px;width:1px;height:185px;background:var(--rule)}
.col-right{left:250px;top:212px;width:200px}
.col-right .head{display:flex;gap:8px;margin-bottom:8px}
.col-right .heading-y{width:156px}
.col-right .lead{margin-bottom:8px}
.person-photo{left:345px;top:382px;width:95px;height:172px;background:linear-gradient(180deg,#e8e2dc 0%,#b7a99e 30%,#2c3553 55%,#1f2742 100%);border-radius:40px 40px 0 0}

.meet-rule{left:24px;top:439px;width:348px;height:1.5px;background:var(--yellow)}
.meet-tag{left:24px;top:441px;background:var(--yellow);font-family:"Montserrat",Arial,sans-serif;font-weight:700;font-size:9.5px;color:var(--ink);padding:2px 16px 2px 4px;clip-path:polygon(0 0,100% 0,88% 100%,0 100%)}
.meet-copy{left:24px;top:464px;width:316px}
.meet-copy p{margin-bottom:8px}

/* footer */
.contact{left:24px;top:568px;width:412px;display:flex;justify-content:space-between;font-weight:700;font-size:6.8px;color:var(--ink)}
.contact__item{display:flex;align-items:center;gap:6px}
.contact__icon{width:15px;height:15px;border-radius:50%;background:var(--ink);display:flex;align-items:center;justify-content:center}

/* back */
.sunset-photo{left:0;top:0;width:460px;height:115px;background:linear-gradient(180deg,#c86a2b 0%,#b9541d 50%,#6e2e10 85%,#2b1208 100%)}
.services-head{left:32px;top:119px}
.services-sub{left:32px;top:133px}
.yellow-field{left:22px;top:338px;width:416px;height:216px;background:var(--yellow);border-bottom:1.5px solid var(--ink)}
.card{background:var(--paper);border-radius:0 0 18px 18px;box-shadow:0 2px 4px rgba(0,0,0,.08)}
.card--benefits{left:22px;top:146px;width:200px;height:220px}
.card--menu{left:237px;top:146px;width:201px;height:220px}
.meeting-photo{left:72px;top:148px;width:98px;height:66px;background:linear-gradient(135deg,#e9eef3 0%,#b8c6d3 50%,#7d8ea3 100%)}
.card .lead{margin-bottom:8px}
.benefits{left:10px;top:74px;width:182px}
.benefits .checks li{margin-bottom:7px}
.menu-title{left:12px;top:6px;width:180px}
.menu-col{top:38px;width:84px}
.menu-col--a{left:12px}
.menu-col--b{left:118px}
.menu-col .checks li{margin-bottom:7px}
.laptop-photo{left:322px;top:380px;width:116px;height:88px;background:radial-gradient(ellipse at 50% 50%,#a08a20 0%,#d8b81c 45%,var(--yellow) 80%)}
.about{left:32px;top:376px;width:270px}
.about .heading-y{color:var(--ink);font-size:10px;margin-bottom:5px}
.about p{margin-bottom:10px}
.pillar{display:flex;gap:9px;align-items:flex-start;width:180px}
.pillar__icon{width:18px;height:18px;border:1.2px solid var(--ink);border-radius:50%;flex:none}
.pillar b{display:block}
.pillar-heart{left:32px;top:456px}
.pillar-mind{left:32px;top:503px}
.pillar-soul{left:255px;top:456px}
.pillar-strength{left:255px;top:503px}
</style>
</head>
<body>

<section class="page page--front">
  <div class="abs hero-photo" role="img" aria-label="Photo of a laptop, phone and plant on a light wooden desk"></div>
  <div class="abs hero-fade"></div>
  <div class="abs brand"><span class="brand__name">BRIGHT LEDGER BOOKKEEPING</span></div>
  <h1 class="abs title">Virtual Bookkeeping<span>for Small Business</span></h1>
  <p class="abs tagline">Build Your Business by Focusing on What You Love</p>
  <div class="abs intro-band">Did you get into business because you loved recording finances? Reconciling bank statements?<br>Prepping for taxes? Of course not! Only nerdy bookkeepers enjoy these things.<br>You want to follow your passion, do what you do best to build a booming business.</div>

  <div class="abs col-left">
    <div class="head"><span class="section-icon"></span><span class="heading-y">Overwhelmed?</span></div>
    <p class="lead">Build your business by focusing on what you love, not what drains the life out of you!</p>
    <ul class="checks">
      <li>Do you feel pulled in so many directions you don't know which way is up?</li>
      <li>Do you hate that shoebox of receipts sitting on your desk?</li>
      <li>Do you wish you could just do the parts of your business that you enjoy?</li>
      <li>Do you dread logging into LedgerDesk?</li>
      <li>Do you panic at tax time?</li>
      <li>Do you feel like you've lost control of your finances?</li>
      <li>Do you wish you could pay yourself more but aren't sure if you can?</li>
    </ul>
  </div>
  <div class="abs divider"></div>
  <div class="abs col-right">
    <div class="head"><span class="section-icon"></span><span class="heading-y">Take charge of your business and concentrate on your strengths to become its hero!</span></div>
    <p class="lead">Outsource your bookkeeping!</p>
    <ul class="checks">
      <li>Take back your time</li>
      <li>Do more of what you love</li>
      <li>Focus on your strengths and what you do best</li>
      <li>Confidently make business decisions</li>
      <li>Sail through tax time</li>
      <li>Save over the expense of a full-time employee</li>
      <li>Pay yourself more</li>
      <li>Experience financial peace</li>
    </ul>
  </div>
  <div class="abs person-photo" role="img" aria-label="Portrait photo of Maya, the bookkeeper, in a navy blouse"></div>
  <div class="abs meet-rule"></div>
  <div class="abs meet-tag">Meet Maya</div>
  <div class="abs meet-copy">
    <p>Hey there! I might be a bookkeeping nerd, but I still love to have some fun! You can catch me hanging out with my family, playing and teaching music, or cruising on my Ridgeway trail bike. I'm also a pro at trip planning and love to hit up the mountains, lakes, and beaches for some R &amp; R time.</p>
    <p>Being a small business owner is tough and I can totally relate. Between bookkeeping and trying to balance business and personal life, it can get overwhelming. I'm all about supporting entrepreneurs and helping small business owners reach their goals. Let's take your business to the next level together!</p>
  </div>
  <div class="abs contact">
    <span class="contact__item"><span class="contact__icon"><svg width="9" height="9" viewBox="0 0 24 24"><path d="M6.6 10.8a15 15 0 006.6 6.6l2.2-2.2a1 1 0 011-.25 11.4 11.4 0 003.6.6 1 1 0 011 1V20a1 1 0 01-1 1A17 17 0 013 4a1 1 0 011-1h3.5a1 1 0 011 1c0 1.25.2 2.45.6 3.6a1 1 0 01-.25 1z" fill="none" stroke="#f9d423" stroke-width="2"/></svg></span>555-014-2290</span>
    <span class="contact__item"><span class="contact__icon"><svg width="9" height="9" viewBox="0 0 24 24"><rect x="3" y="6" width="18" height="12" fill="none" stroke="#f9d423" stroke-width="2"/><path d="M3 6l9 7 9-7" fill="none" stroke="#f9d423" stroke-width="2"/></svg></span>maya@brightledgerbookkeeping.example</span>
    <span class="contact__item"><span class="contact__icon"><svg width="9" height="9" viewBox="0 0 24 24"><circle cx="12" cy="12" r="9" fill="none" stroke="#f9d423" stroke-width="2"/><path d="M3 12h18M12 3c3 3 3 15 0 18M12 3c-3 3-3 15 0 18" fill="none" stroke="#f9d423" stroke-width="1.6"/></svg></span>www.brightledgerbookkeeping.example</span>
  </div>
</section>

<section class="page page--back">
  <div class="abs sunset-photo" role="img" aria-label="Photo of a person in silhouette with arms spread wide against an orange sunset"></div>
  <div class="abs services-head"><span class="heading-y">Services</span></div>
  <p class="abs services-sub">Say Hello to a reliable, hassle-free bookkeeping solution!</p>
  <div class="abs yellow-field"></div>

  <div class="abs card card--benefits">
    <div class="abs benefits">
      <p class="lead">What you get with Bright Ledger Bookkeeping</p>
      <ul class="checks">
        <li>Worry no more about finding time and energy to tackle bookkeeping – Hakuna Matata!</li>
        <li>Keep more of your hard-earned money by maximizing tax deductions – Ka-Ching!</li>
        <li>Understand those confusing financial reports to take your business to the next level – Booyah!</li>
        <li>Celebrate each month's wins during monthly consultations –Hooray!</li>
        <li>Stress-free tax time – Oh Yeah!</li>
      </ul>
    </div>
  </div>
  <div class="abs meeting-photo" role="img" aria-label="Photo of two people reviewing financial charts at a desk"></div>

  <div class="abs card card--menu">
    <div class="abs menu-title"><p class="lead" style="margin-top:6px">Bookkeeping Tailored to YOUR Business Needs</p><p class="lead">Services Available:</p></div>
    <ul class="abs checks menu-col menu-col--a">
      <li>Catch-up and clean-up services</li>
      <li>Transaction importation and categorization</li>
      <li>Monthly reconcilia-tion of all accounts, including assets and loans.</li>
      <li>Monthly financial reports (Balance Sheet, Income Statement, Cash Flow)</li>
      <li>Monthly video conference</li>
    </ul>
    <ul class="abs checks menu-col menu-col--b">
      <li>Annual tax-prep package sent to your preparer</li>
      <li>A/R &amp; A/P</li>
      <li>Payroll coordination</li>
      <li>1099s</li>
      <li>Bill pay and receipt management</li>
      <li>Budgeting</li>
    </ul>
  </div>

  <div class="abs laptop-photo" role="img" aria-label="Yellow-toned photo of a laptop and coffee cup"></div>
  <div class="abs about">
    <h2 class="heading-y">About Us</h2>
    <p>I love the entrepreneurial spirit of small business owners!</p>
    <p class="lead">I want to do more than just help you get by.<br>My goal is to help you succeed and do well in all areas of your life.</p>
  </div>
  <div class="abs pillar pillar-heart"><span class="pillar__icon"></span><span><b>Heart</b>Do what you love and focus on what you do best!</span></div>
  <div class="abs pillar pillar-mind"><span class="pillar__icon"></span><span><b>Mind</b>Finally understand your finances and take control!</span></div>
  <div class="abs pillar pillar-soul"><span class="pillar__icon"></span><span><b>Soul</b>Financial Peace!</span></div>
  <div class="abs pillar pillar-strength"><span class="pillar__icon"></span><span><b>Strength</b>Confidence in business decisions.</span></div>

  <div class="abs contact">
    <span class="contact__item"><span class="contact__icon"><svg width="9" height="9" viewBox="0 0 24 24"><path d="M6.6 10.8a15 15 0 006.6 6.6l2.2-2.2a1 1 0 011-.25 11.4 11.4 0 003.6.6 1 1 0 011 1V20a1 1 0 01-1 1A17 17 0 013 4a1 1 0 011-1h3.5a1 1 0 011 1c0 1.25.2 2.45.6 3.6a1 1 0 01-.25 1z" fill="none" stroke="#f9d423" stroke-width="2"/></svg></span>555-014-2290</span>
    <span class="contact__item"><span class="contact__icon"><svg width="9" height="9" viewBox="0 0 24 24"><rect x="3" y="6" width="18" height="12" fill="none" stroke="#f9d423" stroke-width="2"/><path d="M3 6l9 7 9-7" fill="none" stroke="#f9d423" stroke-width="2"/></svg></span>maya@brightledgerbookkeeping.example</span>
    <span class="contact__item"><span class="contact__icon"><svg width="9" height="9" viewBox="0 0 24 24"><circle cx="12" cy="12" r="9" fill="none" stroke="#f9d423" stroke-width="2"/><path d="M3 12h18M12 3c3 3 3 15 0 18M12 3c-3 3-3 15 0 18" fill="none" stroke="#f9d423" stroke-width="1.6"/></svg></span>www.brightledgerbookkeeping.example</span>
  </div>
</section>

</body>
</html>
```